Vero-Shine Janitorial Services

Looking for a modern design for my new business. I like the clear see through of the card I've attached. The business is built around The Brightwell Omni 720 system, with that said I'd like to add the brightwell logo on the bachside with the statement of Powered by (then the Brightwell Logo). I really like the layout and color schemes of the card I attached. Black, Blue, and White. I would like to incorporate three images into the diamond shape, as seem in the layout.

Martin Okafor
Managing Partner

Still waiting on revisions?

```html
<!DOCTYPE html>
<html lang="en">
<head>
<meta charset="utf-8">
<title>Vero-Shine Janitorial Services – Business Card</title>
<link rel="stylesheet" href="https://fonts.googleapis.com/css2?family=Montserrat:wght@400;500;700&display=swap">
<style>
  :root {
    --backdrop: #d9dbdc;
    --slate: #3c444b;
    --royal: #1b579e;
    --sky: #a9cbe3;
    --bright: #2f8fe0;
    --paper: #f4f5f6;
    --ink: #2b2f33;
    --muted: #6d7a86;
  }
  * { margin: 0; padding: 0; box-sizing: border-box; }
  html, body { width: 1200px; height: 866px; overflow: hidden; }
  body {
    background: var(--backdrop);
    font-family: "Montserrat", Arial, sans-serif;
    position: relative;
  }
  .card {
    position: absolute;
    left: 330px;
    width: 540px;
    height: 308px;
    overflow: hidden;
    box-shadow: 0 6px 18px rgba(0,0,0,.18);
  }
  .card svg { position: absolute; inset: 0; }

  /* Front */
  .card--front { top: 84px; background: var(--slate); }
  .brand { position: absolute; text-align: center; }
  .brand__mark {
    display: block; margin: 0 auto 14px;
    width: 92px; height: 92px; border-radius: 50%;
    background: var(--sky);
  }
  .brand__name, .brand__tag { font-weight: 500; letter-spacing: 1px; }
  .card--front .brand { left: 24px; top: 52px; width: 230px; color: var(--paper); }
  .card--front .brand__name { font-size: 30px; }
  .card--front .brand__tag { font-size: 13px; letter-spacing: 2px; margin-top: 2px; }

  /* Back */
  .card--back { top: 474px; background: var(--paper); }
  .powered {
    position: absolute; left: 26px; top: 28px; color: #fff;
  }
  .powered__label { font-size: 10px; font-weight: 500; letter-spacing: 2.5px; }
  .powered__partner { display: flex; align-items: center; gap: 10px; margin-top: 10px; }
  .powered__name { font-size: 17px; font-weight: 700; }
  .powered__badge { width: 36px; height: 36px; border-radius: 50%; background: #fff; }

  .card--back .brand { right: 34px; top: 22px; width: 190px; color: var(--royal); }
  .card--back .brand__mark { width: 60px; height: 60px; margin-bottom: 8px; }
  .card--back .brand__name { font-size: 22px; }
  .card--back .brand__tag { font-size: 10px; letter-spacing: 1.5px; }

  .contact { position: absolute; left: 190px; top: 186px; right: 34px; }
  .contact__name { color: var(--royal); font-size: 18px; font-weight: 700; letter-spacing: .5px; }
  .contact__role { color: var(--ink); font-size: 13px; margin-top: 2px; }
  .contact__rule { height: 1px; background: var(--sky); margin: 8px 0 10px; }
  .contact__row { display: flex; justify-content: space-between; font-size: 13px; color: var(--ink); }
  .contact__item { display: flex; align-items: center; gap: 6px; }
  .contact__item svg { position: static; width: 14px; height: 14px; }
</style>
</head>
<body>

<section class="card card--front">
  <svg viewBox="0 0 540 308" width="540" height="308">
    <defs>
      <linearGradient id="bucketTone" x1="0" y1="0" x2="1" y2="1">
        <stop offset="0" stop-color="#3a3d42"/><stop offset=".6" stop-color="#d8b21c"/><stop offset="1" stop-color="#8b8f95"/>
      </linearGradient>
      <linearGradient id="sprayTone" x1="0" y1="0" x2="1" y2="1">
        <stop offset="0" stop-color="#aeb4bb"/><stop offset=".5" stop-color="#6f7782"/><stop offset="1" stop-color="#c9ced4"/>
      </linearGradient>
      <linearGradient id="kitTone" x1="0" y1="0" x2="1" y2="1">
        <stop offset="0" stop-color="#2c8be0"/><stop offset=".5" stop-color="#e6ebf0"/><stop offset="1" stop-color="#9fb2c4"/>
      </linearGradient>
    </defs>
    <polygon role="img" aria-label="Photo: cleaner with a yellow mop bucket" points="300,90 395,28 470,100 375,160" fill="url(#bucketTone)" stroke="var(--bright)" stroke-width="3"/>
    <polygon role="img" aria-label="Photo: technician spraying disinfectant from a cart" points="330,230 435,160 530,230 430,305" fill="url(#sprayTone)" stroke="var(--royal)" stroke-width="3"/>
    <polygon role="img" aria-label="Photo: sprayer equipment unit" points="482,100 540,55 540,170 510,165" fill="url(#kitTone)" stroke="var(--bright)" stroke-width="3"/>
  </svg>
  <div class="brand">
    <span class="brand__mark"></span>
    <div class="brand__name">Vero-Shine</div>
    <div class="brand__tag">Janitorial Services</div>
  </div>
</section>

<section class="card card--back">
  <svg viewBox="0 0 540 308" width="540" height="308">
    <path d="M0,0 H300 C140,50 60,180 150,308 H0 Z" fill="var(--royal)"/>
    <path d="M300,0 C150,40 70,170 150,308 H160 C95,190 150,70 320,0 Z" fill="var(--paper)"/>
    <path d="M318,2 C180,50 120,170 175,250 C150,160 210,70 330,4 Z" fill="var(--sky)"/>
  </svg>
  <div class="powered">
    <div class="powered__label">POWERED BY</div>
    <div class="powered__partner">
      <span class="powered__name">Brightwell</span>
      <span class="powered__badge"></span>
    </div>
  </div>
  <div class="brand">
    <span class="brand__mark"></span>
    <div class="brand__name">Vero-Shine</div>
    <div class="brand__tag">Janitorial Services</div>
  </div>
  <div class="contact">
    <div class="contact__name">MARTIN OKAFOR</div>
    <div class="contact__role">Managing Partner</div>
    <div class="contact__rule"></div>
    <div class="contact__row">
      <span class="contact__item">
        <svg viewBox="0 0 24 24"><path d="M6.6 10.8a15 15 0 0 0 6.6 6.6l2.2-2.2a1 1 0 0 1 1-.25 11 11 0 0 0 3.6.6 1 1 0 0 1 1 1V20a1 1 0 0 1-1 1A17 17 0 0 1 3 4a1 1 0 0 1 1-1h3.5a1 1 0 0 1 1 1 11 11 0 0 0 .6 3.6 1 1 0 0 1-.25 1z" fill="none" stroke="var(--royal)" stroke-width="2"/></svg>
        +00 123 456 789
      </span>
      <span class="contact__item">
        <svg viewBox="0 0 24 24"><rect x="3" y="5" width="18" height="14" fill="none" stroke="var(--royal)" stroke-width="2"/><path d="M3 6l9 7 9-7" fill="none" stroke="var(--royal)" stroke-width="2"/></svg>
        office@domain.com
      </span>
    </div>
  </div>
</section>

</body>
</html>
```